Halloway Crest Backers Guild business cards

Create a single-sided business card for the Halloway Crest Backers Guild based on the attached logo.
The additional data fields include Name, Title, Email, Phone, and website.
Please use the following as sample data:
Name: Dean Varrow
Title: Co-Founder / Investor
Email: deanvarrow@mailtern.net
Phone: 555-314-2706
Website: www.hcbackersguild.com

Target Market(s)

Start ups, entrepreneurs, venture capitalists

Industry/Entity Type

Investment

Contact Information for Business Card

Professional business card. Technology company.

Font styles to use
Serif
Sans Serif

Requirements
Must have
• Include the HCBG logo (attached)
• Name
• Title
• Email
• Phone
• Website
Should not have
• Cute, cartoony

```html
<!DOCTYPE html>
<html lang="en">
<head>
<meta charset="utf-8">
<title>Halloway Crest Backers Guild — Business Card</title>
<link rel="stylesheet" href="https://fonts.googleapis.com/css2?family=Source+Sans+3:wght@400;600;700&display=swap">
<style>
  :root {
    --backdrop: #9a9a9b;
    --card-light: #ebebed;
    --card-dark: #3a3a3c;
    --brand-green: #12894a;
    --ink: #3c3c3e;
    --ink-soft: #4a4a4c;
    --rule-dark: #2c2c2e;
    --on-dark: #f2f2f2;
    --on-dark-soft: #cfcfcf;
  }
  * { margin: 0; padding: 0; box-sizing: border-box; }
  html, body {
    width: 1105px;
    height: 1200px;
    overflow: hidden;
    background: var(--backdrop);
    font-family: "Source Sans 3", "Source Sans Pro", sans-serif;
  }
  .card {
    position: absolute;
    left: 182px;
    width: 747px;
    height: 427px;
    overflow: hidden;
  }
  .card--front { top: 119px; background: var(--card-light); }
  .card--back { top: 635px; background: var(--card-dark); }

  .brand {
    position: absolute;
    display: flex;
    align-items: center;
    gap: 16px;
  }
  .brand__mark {
    flex: none;
    border-radius: 50%;
  }
  .brand__name {
    font-weight: 600;
    line-height: 1.1;
  }
  .card--front .brand { left: 60px; top: 213px; transform: translateY(-50%); }
  .card--front .brand__mark { width: 44px; height: 44px; background: var(--brand-green); }
  .card--front .brand__name { font-size: 27px; color: var(--ink); }

  .card--back .brand { left: 50%; top: 85px; transform: translateX(-50%); gap: 26px; }
  .card--back .brand__mark { width: 92px; height: 92px; background: var(--on-dark-soft); }
  .card--back .brand__name { font-size: 42px; color: var(--on-dark); white-space: nowrap; }

  .holder {
    position: absolute;
    left: 424px;
    top: 124px;
  }
  .holder__name {
    font-size: 28px;
    font-weight: 600;
    color: var(--brand-green);
    line-height: 1.1;
  }
  .holder__title {
    font-size: 20px;
    color: var(--ink-soft);
    margin-top: 4px;
  }
  .contact {
    list-style: none;
    margin-top: 22px;
  }
  .contact__item {
    display: flex;
    align-items: center;
    gap: 9px;
    font-size: 19px;
    color: var(--ink-soft);
    height: 29px;
  }
  .contact__icon { width: 18px; height: 18px; flex: none; fill: var(--brand-green); }

  .card__rule {
    position: absolute;
    left: 0; right: 0;
    top: 387px;
    height: 2px;
    background: var(--rule-dark);
  }
  .card__band {
    position: absolute;
    left: 0; right: 0; bottom: 0;
    height: 33px;
    background: var(--brand-green);
  }

  .back__web {
    position: absolute;
    left: 0; right: 0;
    top: 355px;
    text-align: center;
    font-size: 20px;
    letter-spacing: 6px;
    color: var(--on-dark-soft);
  }
</style>
</head>
<body>
  <section class="card card--front">
    <div class="brand">
      <span class="brand__mark"></span>
      <p class="brand__name">Halloway Crest<br>Backers Guild</p>
    </div>

    <div class="holder">
      <p class="holder__name">Dean Varrow</p>
      <p class="holder__title">Co-Founder / Investor</p>
      <ul class="contact">
        <li class="contact__item">
          <svg class="contact__icon" viewBox="0 0 24 24" aria-hidden="true"><path d="M6.6 10.8a15.1 15.1 0 0 0 6.6 6.6l2.2-2.2c.3-.3.7-.4 1-.2 1.1.4 2.3.6 3.6.6.6 0 1 .4 1 1V20c0 .6-.4 1-1 1A17 17 0 0 1 3 4c0-.6.4-1 1-1h3.5c.6 0 1 .4 1 1 0 1.3.2 2.5.6 3.6.1.3 0 .7-.2 1z"/></svg>
          <span>555-314-2706</span>
        </li>
        <li class="contact__item">
          <svg class="contact__icon" viewBox="0 0 24 24" aria-hidden="true"><path d="M2 5h20v14H2z M4 7v.5l8 5 8-5V7l-8 5z" fill-rule="evenodd"/></svg>
          <span>deanvarrow@mailtern.net</span>
        </li>
        <li class="contact__item">
          <svg class="contact__icon" viewBox="0 0 24 24" aria-hidden="true"><circle cx="12" cy="12" r="10"/><path d="M12 2a10 10 0 0 1 0 20M12 2a10 10 0 0 0 0 20M2 12h20M12 2v20" stroke="#ebebed" stroke-width="1.4" fill="none"/></svg>
          <span>www.hcbackersguild.com</span>
        </li>
      </ul>
    </div>

    <div class="card__rule"></div>
    <div class="card__band"></div>
  </section>

  <section class="card card--back">
    <div class="brand">
      <span class="brand__mark"></span>
      <p class="brand__name">Halloway Crest<br>Backers Guild</p>
    </div>
    <p class="back__web">www.hcbackersguild.com</p>
  </section>
</body>
</html>
```